Basketball Training Facility Flyer Design

We need a killer flyer designed for our brand new state of the art basketball training facility here in Syracuse, Utah. This flyer will be distributed to coaches, parents and players in a large school district in Davis and Weber county, Utah. The purpose of the flyer is to announce the launch of the new facility and to encourage parents, coaches and players to come and try out the facility for a free initial session. We're offering a completely complimentary first training session to introduce customers to the facility at no cost.

We use technology and equipment that is typically found in PLH-level training facilities and gymnasiums. Our website can be found here for some additional information - www.corvanhoopworks.com. Customers can easily book and pay online through our website (the functionality will be done by the time we distribute the completed flyer).

The design needs to highlight the equipment we offer at the facility, because no other basketball training center has the same level of technology we do. We want the flyer to be clean and simple.

Please see must haves for specific details.

The size of the flyer we want to print is 5.75 inches by 9.5 inches.

Target Market(s)

Parents of basketball players of all skill levels age 8-18.

Industry/Entity Type

Training

Requirements
Must have
• Design must include this header: You want to dominate on the court. We have the formula to make that happen.

Design must include this sub header or highlight: Free Introductory Training Session!

The design must include our Logo

The design must include the photos attached of the Rebo, the Jumplora and the Dribtek

Under the the photo of the Rebo 4200 (attached) please include this verbiage:
Game Shots in Game Spots at Game Speed

Under the photo of the Jumplora (see attached) please include this verbiage:
Improve Power, Agility and Speed like Never Before

Under the photo of the Dribtek (attached) please include this verbiage:
Real Time Statistics to Improve Dribble Speed, Accuracy and Right / Left Comparison

Include this verbiage somewhere in the design: Technology Used by PLH and the Best D-1 College Teams

The design must include a strong call to action: Call or Click Now to Schedule A Free Training Session!

The design must include our contact information in easy-to-read font and size (also specifically highlighting the website):

Schedule Online in Less Than 60 Seconds!
Call or Click
801-482-7195
www.corvanhoopworks.com
Nice to have
• For examples of the type of design we like, please see the attached images labeled

Please use stock photos of your preference to go in the flyer (preferably images of youth basketball training or kids in basketball training)

We don't want the flyer to be too cluttered, so please use images at your discretion.

Thank you!

```html
<!DOCTYPE html>
<html lang="en">
<head>
<meta charset="utf-8">
<title>Corvan Hoopworks – Free Training Session Flyer</title>
<link href="https://fonts.googleapis.com/css2?family=Arimo:wght@400;700&display=swap" rel="stylesheet">
<style>
  :root {
    --stage: #a9835c;
    --flyer-black: #1b1b1b;
    --flyer-dark: #262626;
    --orange: #f7931e;
    --orange-deep: #e07812;
    --white: #ffffff;
    --bar-top: #5a5a5a;
    --bar-bottom: #2e2e2e;
    --frame: #3a3a3a;
    --frame-edge: #555555;
  }
  * { margin: 0; padding: 0; box-sizing: border-box; }
  html, body { width: 1200px; height: 900px; overflow: hidden; }
  body {
    background: var(--stage);
    font-family: "Arimo", Arial, sans-serif;
    position: relative;
  }
  .flyer {
    position: absolute;
    left: 365px; top: 60px;
    width: 470px; height: 776px;
    background: radial-gradient(ellipse at 50% 45%, #2c2c2c 0%, var(--flyer-black) 70%);
    box-shadow: 0 6px 18px rgba(0,0,0,.45);
    overflow: hidden;
    color: var(--white);
  }
  .brand-ribbon {
    position: absolute; left: 20px; top: 0;
  }
  .brand-ribbon .brand-name {
    position: absolute; left: 0; top: 140px; width: 78px;
    text-align: center; font-weight: 700; font-size: 11px; line-height: 1.25;
    color: var(--white); text-transform: uppercase;
  }
  .brand-watermark {
    position: absolute; left: 97px; top: 235px;
    width: 290px; height: 290px; border-radius: 50%;
    border: 14px solid rgba(255,255,255,.045);
    display: flex; align-items: center; justify-content: center;
  }
  .brand-watermark span {
    font-weight: 700; font-size: 28px; letter-spacing: 2px; text-align: center;
    color: rgba(255,255,255,.05); text-transform: uppercase; line-height: 1.2;
  }
  .headline { position: absolute; left: 117px; top: 18px; width: 330px; }
  .headline .line {
    display: block; font-weight: 700; white-space: nowrap;
    border-bottom: 3px solid var(--white); padding-bottom: 1px; margin-bottom: 4px;
    line-height: 1;
  }
  .headline .small { font-size: 14px; color: var(--white); }
  .headline .big { color: var(--orange); text-transform: uppercase; }
  .line-you { width: 146px; } .line-you .big { font-size: 29px; }
  .line-dominate { width: 315px; } .line-dominate .big { font-size: 50px; letter-spacing: -.5px; }
  .line-court { width: 220px; } .line-court .big { font-size: 29px; }
  .line-formula { width: 330px; } .line-formula .big { font-size: 32px; }
  .line-happen { width: 285px; } .line-happen .big { font-size: 32px; }
  .bar {
    position: absolute; display: flex; align-items: center;
    background: linear-gradient(var(--bar-top), var(--bar-bottom));
    box-shadow: 0 2px 4px rgba(0,0,0,.5); font-weight: 700;
  }
  .tech-claim { left: 20px; top: 323px; width: 430px; height: 29px; padding-left: 6px; font-size: 13px; }
  .offer-label { position: absolute; left: 23px; top: 384px; font-size: 12px; font-weight: 700; }
  .cta { left: 0; color: var(--orange); padding-left: 20px; }
  .cta-one { top: 403px; width: 243px; height: 37px; font-size: 24px; }
  .cta-two { top: 448px; width: 225px; height: 35px; font-size: 19px; }
  .equipment { position: absolute; left: 0; top: 524px; width: 470px; }
  .equipment .caption {
    position: absolute; font-size: 7.5px; font-weight: 700; text-align: center; line-height: 1.2;
  }
  .equipment .frame {
    position: absolute; top: 36px; height: 102px;
    background: linear-gradient(var(--frame-edge), var(--frame));
    padding: 8px 10px; box-shadow: 0 3px 6px rgba(0,0,0,.6);
  }
  .equipment .photo { width: 100%; height: 100%; }
  .floor-glow {
    position: absolute; left: 0; top: 662px; width: 470px; height: 26px;
    background: linear-gradient(rgba(240,150,60,.35), rgba(0,0,0,0));
  }
  .contact { position: absolute; left: 24px; top: 692px; font-weight: 700; line-height: 17px; font-size: 14px; }
  .contact .accent { color: var(--orange); }
  .contact .web { font-size: 15px; }
</style>
</head>
<body>
<main class="flyer">
  <div class="brand-watermark"><span>Corvan<br>Hoopworks</span></div>

  <div class="brand-ribbon">
    <svg width="78" height="302" viewBox="0 0 78 302" aria-hidden="true">
      <defs>
        <linearGradient id="ribbonTone" x1="0" x2="1">
          <stop offset="0" stop-color="#f28a18"/><stop offset=".5" stop-color="#f9a23a"/><stop offset="1" stop-color="#e57a10"/>
        </linearGradient>
      </defs>
      <polygon points="0,0 78,0 78,302 39,270 0,302" fill="url(#ribbonTone)"/>
      <circle cx="39" cy="95" r="8" fill="#ffffff" opacity=".9"/>
    </svg>
    <div class="brand-name">Corvan<br>Hoopworks</div>
  </div>

  <h1 class="headline">
    <span class="line line-you"><span class="big">You</span> <span class="small">want to</span></span>
    <span class="line line-dominate"><span class="big">Dominate</span></span>
    <span class="line line-court"><span class="small">on the</span> <span class="big">Court ?</span></span>
    <span class="line line-formula"><span class="big">We</span> <span class="small">have the</span> <span class="big">Formula</span></span>
    <span class="line line-happen"><span class="small">to make thath</span> <span class="big">Happen</span></span>
  </h1>

  <p class="bar tech-claim">Technology Used by PLH and the Best D-1 College Teams</p>

  <p class="offer-label">Free Introductory Training Session!</p>
  <p class="bar cta cta-one">Schedule A Free</p>
  <p class="bar cta cta-two">Training Session!</p>

  <section class="equipment">
    <p class="caption" style="left:18px;top:10px;width:92px;">Game Shots in Game Spots at Game Speed</p>
    <p class="caption" style="left:155px;top:0;width:170px;">Real Time Statistics<br>to Improve Dribble Speed,<br>Accuracy and Right / Left Comparison</p>
    <p class="caption" style="left:370px;top:0;width:84px;">Improve Power,<br>Agility and Speed<br>like Never Before</p>

    <div class="frame" style="left:17px;width:134px;">
      <div class="photo" role="img" aria-label="Photo of the Rebo 4200 shooting machine" style="background:linear-gradient(#ffffff,#e9dcd6);"></div>
    </div>
    <div class="frame" style="left:168px;width:132px;">
      <div class="photo" role="img" aria-label="Photo of the Dribtek smart basketball with phone app" style="background:radial-gradient(circle at 45% 55%,#b04a22 0%,#d9a48a 30%,#ffffff 55%);"></div>
    </div>
    <div class="frame" style="left:317px;width:136px;">
      <div class="photo" role="img" aria-label="Photo of an athlete training on the Jumplora platform" style="background:linear-gradient(#ffffff,#c9d3e4);"></div>
    </div>
  </section>

  <div class="floor-glow"></div>

  <address class="contact" style="font-style:normal;">
    <p>Schedule Online in Less Than 60 Seconds!</p>
    <p class="accent">Call or Click</p>
    <p>801-482-7195</p>
    <p class="accent web">www.corvanhoopworks.com</p>
  </address>
</main>
</body>
</html>
```